Managed Service Provider need new business cards

We are a small Maanged Service Provider of IT Services and need a new fresh design for our business cards. We want something impossible, fun and professional :)
Our services has a large range, but we are always fun and make sure our customers both get their issue sorted and also feel like they are "catching up with an old friend".
All our cards in the past has always been all black, with red and we need something fresher.
The back of card, we would like just a small list of what we do i think, but if someone has a better idea, please do something cool with the back of the card:
Managed IT Services
Productivity Solutions
Data Backup and Recovery
IT System Maintenance
Managed IT Security
More details can be found on our website tqnetworks.com.au
Industry/Entity Type
It Company
Contact Information for Business Card
Name: Dwayne Falstrup
Title: Director
Phone: 03 6193 4827
Mobile: 0412 587 239
Email: dwayne@tqnetworks.com.au
Web: www.tqnetworks.com.au

```html
<!DOCTYPE html>
<html lang="en">
<head>
<meta charset="utf-8">
<title>TQ Networks — Business Card</title>
<link rel="stylesheet" href="https://fonts.googleapis.com/css2?family=Jost:wght@400;500;600;700&display=swap">
<style>
  :root {
    --canvas: #f2f2f2;
    --card-front: #efefef;
    --card-front-light: #f7f7f7;
    --brand-red: #e8202a;
    --back-red: #ec1a45;
    --white: #ffffff;
  }
  * { margin: 0; padding: 0; box-sizing: border-box; }
  html, body {
    width: 1200px; height: 1200px; overflow: hidden;
    background: var(--canvas);
    font-family: "Jost", sans-serif;
  }
  .canvas { position: relative; width: 1200px; height: 1200px; }

  /* Front card */
  .card-front {
    position: absolute; left: 208px; top: 108px; width: 767px; height: 447px;
    background: var(--card-front);
    overflow: hidden;
  }
  .card-front .texture {
    position: absolute; inset: 0;
    background: linear-gradient(135deg, var(--card-front-light) 0%, var(--card-front) 50%, var(--card-front-light) 100%);
  }
  .front-brand {
    position: absolute; left: 0; right: 0; top: 196px;
    display: flex; align-items: center; justify-content: center; gap: 16px;
    white-space: nowrap;
  }
  .brand-dot {
    flex: none;
    width: 30px; height: 30px; border-radius: 50%;
    background: var(--brand-red);
  }
  .front-brand .brand-name {
    font-weight: 700; font-size: 56px; letter-spacing: 1px;
    color: var(--brand-red); line-height: 1;
  }
  .web-band {
    position: absolute; left: 0; bottom: 0; width: 100%; height: 28px;
    background: var(--brand-red);
    display: flex; align-items: center; justify-content: center;
  }
  .web-band span {
    color: var(--white); font-size: 11px; letter-spacing: 14.5px; font-weight: 500;
    white-space: nowrap;
  }

  /* Back card */
  .card-back {
    position: absolute; left: 217px; top: 620px; width: 750px; height: 445px;
    background: var(--back-red);
    color: var(--white);
    overflow: hidden;
  }
  .contact-name {
    position: absolute; left: 42px; top: 36px;
    font-size: 20px; font-weight: 600; letter-spacing: 1px; white-space: nowrap;
  }
  .contact-title {
    position: absolute; left: 42px; top: 63px; font-size: 11px; font-weight: 400;
  }
  .contact-list { position: absolute; left: 42px; top: 104px; list-style: none; white-space: nowrap; }
  .contact-list li { font-size: 12px; line-height: 23px; }
  .contact-list li.phone { font-size: 15px; letter-spacing: .3px; }
  .contact-list b { font-weight: 600; font-size: 10px; display: inline-block; width: 14px; }

  .back-brand {
    position: absolute; left: 308px; top: 186px;
    display: flex; align-items: center; gap: 14px;
    white-space: nowrap;
  }
  .back-brand .brand-dot { background: var(--white); width: 28px; height: 28px; }
  .back-brand .brand-name {
    font-weight: 700; font-size: 46px; letter-spacing: 1px; line-height: 1; color: var(--white);
  }

  .services-heading {
    position: absolute; left: 398px; top: 280px;
    font-size: 14px; font-weight: 600; letter-spacing: 2px; white-space: nowrap;
  }
  .services {
    position: absolute; left: 0; width: 756px; top: 332px;
    list-style: none; text-align: center; white-space: nowrap;
  }
  .services li { font-size: 15px; letter-spacing: 1.9px; line-height: 27.5px; }
</style>
</head>
<body>
<main class="canvas">

  <section class="card-front">
    <div class="texture" role="img" aria-label="Faint light grey low-poly geometric pattern"></div>
    <div class="front-brand">
      <span class="brand-dot"></span>
      <span class="brand-name">TQ NETWORKS</span>
    </div>
    <div class="web-band"><span>www.tqnetworks.com.au</span></div>
  </section>

  <section class="card-back">
    <h1 class="contact-name">DWAYNE FALSTRUP</h1>
    <p class="contact-title">Managing Director</p>
    <ul class="contact-list">
      <li class="phone"><b>T</b>: 03 6193 4827 &nbsp;, 0412 587 239</li>
      <li><b>E</b>: dwayne@tqnetworks.com.au</li>
      <li><b>W</b>: www.tqnetworks.com.au</li>
    </ul>

    <div class="back-brand">
      <span class="brand-name">TQ NETWORKS</span>
      <span class="brand-dot"></span>
    </div>

    <h2 class="services-heading">Our Services</h2>
    <ul class="services">
      <li>-Managed IT Services &nbsp;- Productivity Solutions</li>
      <li>- Data Backup and Recovery- IT System Maintenance</li>
      <li>- Managed IT Security</li>
    </ul>
  </section>

</main>
</body>
</html>
```